Business Card Design Project

Build kick ass business card.
Updates

I just uploaded the Veruxo Logo in AI format, for those that were asking. It's looking real good and we'll be reviewing the designs soon. Thanks. 

Target Market(s)

Businesses in many verticals. Focusing on information security.

Veruxo, LLC
Darren Colby
Principal Security Consultant
Mobile: +1-480-555-0137
Email: Darren.Colby@Veruxo.example
Web: www.veruxo.example

Industry/Entity Type

Business

Requirements
Must have
• Design must look high-end, hi-tech stylish and minimalist

Be different – one that stands out from thousands of others

Does not have to be traditional rectangle

Would like logo integrated

```html
<!DOCTYPE html>
<html lang="en">
<head>
<meta charset="utf-8">
<title>Veruxo, LLC — Darren Colby</title>
<link rel="stylesheet" href="https://fonts.googleapis.com/css2?family=Open+Sans:wght@400&display=swap">
<style>
  :root {
    --paper: #ffffff;
    --ink: #111111;
    --brand-ink: #1f1f1f;
    --title-slate: #3f5d72;
    --accent-blue: #2b7fc3;
    --accent-cyan: #3fc8dc;
  }
  html, body {
    margin: 0;
    padding: 0;
    overflow: hidden;
    background: var(--paper);
  }
  .card {
    position: relative;
    width: 825px;
    height: 1200px;
    background: var(--paper);
    font-family: "Open Sans", sans-serif;
    color: var(--ink);
    overflow: hidden;
  }
  .brand {
    position: absolute;
    left: 150px;
    top: 218px;
    display: flex;
    align-items: center;
    gap: 42px;
  }
  .brand-dot {
    width: 120px;
    height: 120px;
    border-radius: 50%;
    background: var(--accent-cyan);
  }
  .brand-name {
    font-size: 84px;
    font-weight: 400;
    letter-spacing: 6px;
    color: var(--brand-ink);
    line-height: 1;
  }
  .identity {
    position: absolute;
    left: 92px;
    top: 664px;
  }
  .company {
    margin: 0;
    font-size: 46px;
    font-weight: 400;
    line-height: 1.2;
  }
  .person {
    margin: 14px 0 0;
    font-size: 33px;
    font-weight: 400;
    line-height: 1.2;
  }
  .role {
    margin: 4px 0 0;
    font-size: 29px;
    font-weight: 400;
    color: var(--title-slate);
    line-height: 1.2;
  }
  .contacts {
    position: absolute;
    left: 94px;
    top: 908px;
    margin: 0;
    padding: 0;
    list-style: none;
  }
  .contact {
    font-size: 36px;
    line-height: 1.2;
    margin-bottom: 14px;
    white-space: nowrap;
  }
  .contact--web { font-size: 40px; margin-bottom: 12px; }
  .contact--phone { font-size: 34px; }
  .contact-mark {
    color: var(--accent-blue);
    margin-right: 8px;
  }
  .contact--phone .contact-mark { margin-right: 0; }
</style>
</head>
<body>
  <main class="card">
    <div class="brand">
      <span class="brand-dot" aria-hidden="true"></span>
      <span class="brand-name">VERUXO</span>
    </div>

    <section class="identity">
      <h1 class="company">Veruxo, LLC</h1>
      <p class="person">Darren Colby</p>
      <p class="role">Principal Security Consultant</p>
    </section>

    <ul class="contacts">
      <li class="contact contact--web"><span class="contact-mark">W|</span>www.veruxo.example</li>
      <li class="contact contact--mail"><span class="contact-mark">@|</span>Darren.Colby@Veruxo.example</li>
      <li class="contact contact--phone"><span class="contact-mark">m|</span>+1-480-555-0137</li>
    </ul>
  </main>
</body>
</html>
```